Consulting firm needs elegant, modern designs

Business card design - I have a logo which has previously been developed for Q-Pathways - I will attach. I will also attach specifications for the size of the business card.

We also need a logo design for our leadership consulting product - Form in Guidance - we focus on improving workplace health by educating leaders and learning professionals about how the physical and emotional affects performance and engagement. I have some example logos and ideas which I will attach - these have attempted to bring in the body but I do not like the font (see www.formingguidance-example.com for preferred font). Idea is to please have a 'body' visible somehow in the word Leadership, ensuring that this conveys flexibility and agility. Colors which I prefer are deep purple OR turquoise, together with silver. COLORS below are for LOGO design.

Target Market(s)

For the business card, it should be more masculine. The logo which will be attached should be neutralized into dark blue shades and silver. The business card Q-Pathways is focused on business transformation - organizations who would require a consultant to help them enter new markets, for example.

Industry/Entity Type

Leadership

Contact Information for Business Card

Content:
Q-Pathways
Lindenkade 27
4921KP, Breda, The Netherlands
maurits@Q-Pathways.example
www.Q-Pathways.example

Colors for business card should be conservative and slightly more masculine. Use the Q-Pathways logo but change the colors to blue or shades of gray/black.

Dimensions for cut
85 x 55 mm
1004 x 650 pixels
Full document size
88 x 58 mm
1040 x 685 pixels
For the best result, you need to design the full document size including the bleed

Logo Text

Form in Guidance

Font styles to use
Serif
Sans Serif

Colors
876aae
333333
959595

Requirements
Must have
• Professional, modern and unique business card design
• Professional, elegant, and modern logo design - with creative thinking
Should not have
• Too many colors

```html
<!DOCTYPE html>
<html lang="en">
<head>
<meta charset="utf-8">
<title>Q-Pathways business card</title>
<link href="https://fonts.googleapis.com/css2?family=Montserrat:wght@400;600;700&family=Open+Sans:wght@400;600&display=swap" rel="stylesheet">
<style>
  :root {
    --stage: #2b2b2e;
    --card-dark: #2a2458;
    --card-dark-deep: #221d4a;
    --card-light: #ffffff;
    --ink: #2e2a4a;
    --ink-soft: #55535f;
    --accent-purple: #4a43a0;
    --accent-blue: #3a6fae;
    --accent-teal: #4fb3b0;
  }
  * { margin: 0; padding: 0; box-sizing: border-box; }
  html, body { width: 1200px; height: 930px; overflow: hidden; }
  body {
    background: var(--stage);
    position: relative;
    font-family: "Open Sans", Arial, sans-serif;
  }
  .card {
    position: absolute;
    width: 560px;
    height: 362px;
    border-radius: 2px;
    overflow: hidden;
    box-shadow: 0 10px 30px rgba(0,0,0,.45);
  }
  .card-front {
    left: 60px; top: 70px;
    background: linear-gradient(100deg, var(--card-dark-deep) 0%, var(--card-dark) 45%, #2d2860 100%);
  }
  .card-front .gloss {
    position: absolute; left: 150px; top: 0; width: 22px; height: 100%;
    background: linear-gradient(90deg, rgba(255,255,255,0) 0%, rgba(255,255,255,.08) 50%, rgba(255,255,255,0) 100%);
  }
  .card-back {
    left: 580px; top: 480px;
    background: var(--card-light);
  }
  .brand {
    position: absolute;
    display: flex;
    align-items: center;
    gap: 14px;
  }
  .brand-dot {
    width: 46px; height: 46px; border-radius: 50%;
    background: var(--accent-teal);
    flex: none;
  }
  .brand-name {
    font-family: "Montserrat", Arial, sans-serif;
    font-weight: 600;
    font-size: 40px;
    line-height: 1;
    letter-spacing: .5px;
  }
  .card-front .brand { left: 40px; bottom: 56px; }
  .card-front .brand-name { color: #ffffff; }
  .card-back .brand { left: 40px; top: 72px; }
  .card-back .brand-name { color: var(--ink); font-size: 36px; }
  .card-back .brand-dot { width: 42px; height: 42px; }

  .holder {
    position: absolute; right: 40px; top: 140px; text-align: right;
  }
  .holder-name {
    font-family: "Montserrat", Arial, sans-serif;
    font-weight: 700; font-size: 25px; letter-spacing: 2px;
    color: var(--accent-purple);
  }
  .holder-role {
    font-family: "Montserrat", Arial, sans-serif;
    font-weight: 700; font-size: 11px; letter-spacing: 1.5px;
    color: #1f1f24;
  }
  .divider {
    position: absolute; left: 40px; right: 40px; top: 206px;
    height: 1px; background: var(--accent-purple);
  }
  .contact {
    position: absolute; left: 40px; top: 248px;
    list-style: none; font-size: 14px; color: var(--ink-soft);
  }
  .contact li { display: flex; align-items: center; gap: 10px; line-height: 22px; }
  .contact svg { width: 13px; height: 13px; flex: none; }
  .address {
    position: absolute; right: 40px; top: 220px; text-align: right;
    font-style: normal; font-size: 13px; color: var(--ink-soft); line-height: 20px;
  }
  .address .company { color: var(--accent-blue); font-weight: 600; }
  .band { position: absolute; left: 0; bottom: 0; width: 560px; height: 40px; }
</style>
</head>
<body>
  <section class="card card-front" aria-label="Card front">
    <div class="gloss"></div>
    <div class="brand">
      <span class="brand-dot"></span>
      <div class="brand-name">Q-Pathways</div>
    </div>
  </section>

  <section class="card card-back" aria-label="Card back">
    <div class="brand">
      <span class="brand-dot"></span>
      <div class="brand-name">Q-Pathways</div>
    </div>

    <div class="holder">
      <div class="holder-name">ARLEN VOSS</div>
      <div class="holder-role">CEO</div>
    </div>

    <div class="divider"></div>

    <address class="address">
      <div class="company">Q-Pathways</div>
      <div>Lindenkade 27</div>
      <div>4921KP, Breda, The Netherlands</div>
    </address>

    <ul class="contact">
      <li>
        <svg viewBox="0 0 14 14" fill="none" stroke="#4a43a0" stroke-width="1.4"><rect x="1" y="3" width="12" height="8"/><path d="M1 3l6 5 6-5"/></svg>
        maurits@Q-Pathways.example
      </li>
      <li>
        <svg viewBox="0 0 14 14" fill="none" stroke="#4a43a0" stroke-width="1.2"><circle cx="7" cy="7" r="6"/><path d="M1 7h12M7 1c-3 3-3 9 0 12M7 1c3 3 3 9 0 12"/></svg>
        www.Q-Pathways.example
      </li>
    </ul>

    <svg class="band" viewBox="0 0 560 40" preserveAspectRatio="none" aria-hidden="true">
      <defs>
        <linearGradient id="bandBlue" x1="0" x2="1">
          <stop offset="0" stop-color="#3a6fae"/>
          <stop offset="1" stop-color="#5f86c0"/>
        </linearGradient>
      </defs>
      <polygon points="0,32 330,12 318,40 0,40" fill="url(#bandBlue)"/>
      <polygon points="340,12 560,0 560,40 326,40" fill="#4a43a0"/>
    </svg>
  </section>
</body>
</html>
```